Marlowen

I'm looking for business cards with the logo I've attached. I don't have an specific idea in mind and open to anything. All the usual info will be involved. Name, position in company, nr, email, address

```html
<!DOCTYPE html>
<html lang="en">
<head>
<meta charset="utf-8">
<title>Marlowen Designs – Business Cards</title>
<link href="https://fonts.googleapis.com/css2?family=Roboto:wght@300;400;700&display=swap" rel="stylesheet">
<style>
  :root {
    --page-bg: #e4e5e7;
    --navy: #172c4a;
    --navy-deep: #0b1626;
    --navy-mid: #13233d;
    --gold: #ecb33c;
    --white: #ffffff;
    --ink: #1d2d47;
  }
  * { margin: 0; padding: 0; box-sizing: border-box; }
  html, body {
    width: 1200px; height: 1200px; overflow: hidden;
    background: var(--page-bg);
    font-family: "Roboto", Arial, sans-serif;
  }
  .canvas { position: relative; width: 1200px; height: 1200px; }

  .card {
    position: absolute;
    width: 660px; height: 432px;
    border-radius: 34px;
    overflow: hidden;
  }

  /* Front */
  .card--front {
    left: 270px; top: 110px;
    background: radial-gradient(circle at 78% 88%, #10284a 0%, var(--navy-mid) 45%, var(--navy-deep) 100%);
    display: flex; align-items: center; justify-content: center;
  }
  .brand {
    display: flex; align-items: center; gap: 22px;
    color: var(--gold); font-weight: 700;
  }
  .brand__dot {
    width: 46px; height: 46px; border-radius: 50%;
    background: var(--gold);
  }
  .brand__name { line-height: 1; text-transform: uppercase; }
  .brand__name .line-1 { display: block; font-size: 58px; letter-spacing: 1px; }
  .brand__name .line-2 { display: block; font-size: 28px; letter-spacing: 17px; margin-top: 14px; }

  /* Back */
  .card--back {
    left: 270px; top: 650px;
    background: var(--white);
  }
  .card--back .brand {
    position: absolute; left: 30px; top: 130px; gap: 16px;
  }
  .card--back .brand__dot { width: 36px; height: 36px; }
  .card--back .brand__name .line-1 { font-size: 48px; }
  .card--back .brand__name .line-2 { font-size: 24px; letter-spacing: 15px; margin-top: 12px; }

  .holder {
    position: absolute; right: 36px; top: 72px; text-align: right;
  }
  .holder__company { color: var(--gold); font-weight: 700; font-size: 30px; }
  .holder__role { color: var(--ink); font-weight: 400; font-size: 19px; margin-top: 4px; }

  .wave { position: absolute; left: 0; top: 0; width: 660px; height: 432px; }

  .contacts { position: absolute; right: 0; top: 284px; }
  .contact {
    display: flex; align-items: center; justify-content: flex-end;
    height: 34px; margin-bottom: 9px;
  }
  .contact__text { color: var(--white); font-weight: 300; font-size: 20px; margin-right: 16px; }
  .contact__text--phone { font-weight: 700; font-size: 28px; }
  .contact__tab {
    width: 64px; height: 34px;
    background: var(--gold);
    border-radius: 17px 0 0 17px;
    display: flex; align-items: center; padding-left: 12px;
  }
  .contact__tab svg { width: 18px; height: 18px; }
</style>
</head>
<body>
<main class="canvas">

  <section class="card card--front" aria-label="Card front">
    <div class="brand">
      <span class="brand__dot"></span>
      <span class="brand__name"><span class="line-1">Marlowen</span><span class="line-2">Designs</span></span>
    </div>
  </section>

  <section class="card card--back" aria-label="Card back">
    <svg class="wave" viewBox="0 0 660 432" aria-hidden="true">
      <path d="M0 344 C 170 272, 380 258, 516 260 C 600 262, 640 266, 660 270 L660 432 L0 432 Z" fill="var(--navy)"/>
    </svg>

    <div class="brand">
      <span class="brand__dot"></span>
      <span class="brand__name"><span class="line-1">Marlowen</span><span class="line-2">Designs</span></span>
    </div>

    <div class="holder">
      <p class="holder__company">KB Waste Haulage</p>
      <p class="holder__role">Managing Director</p>
    </div>

    <div class="contacts">
      <div class="contact">
        <span class="contact__text contact__text--phone">0412 730 961</span>
        <span class="contact__tab">
          <svg viewBox="0 0 24 24"><path fill="var(--navy)" d="M6.6 10.8a15.2 15.2 0 0 0 6.6 6.6l2.2-2.2a1 1 0 0 1 1-.25 11.4 11.4 0 0 0 3.6.6 1 1 0 0 1 1 1V20a1 1 0 0 1-1 1A17 17 0 0 1 3 4a1 1 0 0 1 1-1h3.5a1 1 0 0 1 1 1c0 1.25.2 2.45.6 3.6a1 1 0 0 1-.25 1z"/></svg>
        </span>
      </div>
      <div class="contact">
        <span class="contact__text">hello@marlowenstudio.com.au</span>
        <span class="contact__tab">
          <svg viewBox="0 0 24 24"><circle cx="12" cy="12" r="4" fill="none" stroke="var(--navy)" stroke-width="2.4"/><path d="M16 8v5.5a2.5 2.5 0 0 0 5 0V12a9 9 0 1 0-3.5 7.1" fill="none" stroke="var(--navy)" stroke-width="2.4"/></svg>
        </span>
      </div>
      <div class="contact">
        <span class="contact__text">www.marlowendesigns.com.au</span>
        <span class="contact__tab">
          <svg viewBox="0 0 24 24" fill="none" stroke="var(--navy)" stroke-width="2"><circle cx="12" cy="12" r="9"/><ellipse cx="12" cy="12" rx="4" ry="9"/><path d="M3 12h18M5 7h14M5 17h14"/></svg>
        </span>
      </div>
    </div>
  </section>

</main>
</body>
</html>
```